Spa Business Card Design Project

Hello! We are a boutique spa for men and women that is rebranding. I would like a memorable new business card that showcases our beautiful new logo and our unique business. I would like it to be classic/timeless and eclectic/artistic at the  same time.
I am a fan of negative space as you can tell from the logo. I am also open to any creative ideas.
Multi sided design. Two sided design is acceptable as an option, too. "Flaps/folds/whatever the design term is" are optional- whether full vertical or horizontal, half flap, full flap etc
On either side next to the golden snail I would potentially like to see "slow down. Enjoy Life."  Possibly on one statment on top of each other, crowned with the snail. Or the statment following the snail on one line... I am open for a creative suprise, too.
The back I would like room for the standard Information
"3817 Birch Lane
linden vale, new york 10999
(555) 462 3085
info@thecorvella spa.com
The snail is to be done in gold ink.
Can I also Have an option for cards that are individualized for staff members, too?

Updates
Project Deadline Extended
Reason: I apologize for the deadline extension. My day was more involved than anticipated in other matters. Hope to have this closed by next Tuesday.
Thank you

Target Market(s)
Men and women with expendable income between the ages of 30-55
Industry/Entity Type
Boutique
Requirements
Must have
- only black and gold ink.

Nice to have
- One of a kind.
Showcase the snail :-)
make you smile :-)
Fun, but professional.
Should not have
- Lots of color.
Too feminine.
Too busy.

```html
<!DOCTYPE html>
<html lang="en">
<head>
<meta charset="utf-8">
<title>The Corvella Spa — Business Card Set</title>
<link rel="stylesheet" href="https://fonts.googleapis.com/css2?family=Cinzel:wght@400;500&family=Questrial&display=swap">
<style>
  :root {
    --backdrop: #4e4641;
    --sleeve: #5c534b;
    --kraft-light: #cbbca6;
    --kraft-mid: #b9a88f;
    --kraft-dark: #9c8a72;
    --ink: #141210;
    --paper-white: #f4f1ec;
    --gold: #c99a1e;
  }
  * { box-sizing: border-box; margin: 0; padding: 0; }
  html, body { width: 1200px; height: 900px; overflow: hidden; }
  body { background: var(--backdrop); position: relative; font-family: "Questrial", sans-serif; }

  .piece { position: absolute; width: 337px; height: 217px; box-shadow: 0 1px 4px rgba(0,0,0,.45); }

  .card {
    background: radial-gradient(ellipse 75% 70% at 50% 45%, var(--kraft-light) 0%, var(--kraft-mid) 60%, var(--kraft-dark) 100%);
    color: var(--ink);
    overflow: hidden;
  }

  .sleeve {
    background: var(--sleeve);
    color: var(--paper-white);
    -webkit-mask: radial-gradient(circle at 0 28px, transparent 12px, #000 12.5px),
                  radial-gradient(circle at 74px 108px, transparent 53px, #000 53.5px);
    -webkit-mask-composite: source-in;
    mask: radial-gradient(circle at 0 28px, transparent 12px, #000 12.5px),
          radial-gradient(circle at 74px 108px, transparent 53px, #000 53.5px);
    mask-composite: intersect;
  }
  .sleeve.plain { -webkit-mask: none; mask: none; }

  .wordmark { position: absolute; text-align: center; font-family: "Cinzel", serif; font-weight: 400; line-height: 1; }
  .wordmark .name { display: block; letter-spacing: .02em; white-space: nowrap; }
  .wordmark .line { display: block; }
  .wordmark .descriptor { display: block; font-family: "Questrial", sans-serif; white-space: nowrap; margin-top: 3px; }

  .wordmark.small { width: 100px; }
  .wordmark.small .name { font-size: 13px; }
  .wordmark.small .descriptor { font-size: 5px; }

  .wordmark.large { width: 220px; }
  .wordmark.large .name { font-size: 24px; }
  .wordmark.large .descriptor { font-size: 8px; margin-top: 5px; }

  .wordmark.medium { width: 180px; }
  .wordmark.medium .name { font-size: 20px; }
  .wordmark.medium .descriptor { font-size: 7px; margin-top: 4px; }

  .motto { position: absolute; display: flex; align-items: center; gap: 4px; font-family: "Cinzel", serif; font-size: 8px; letter-spacing: .02em; white-space: nowrap; }
  .motto .lead { display: inline-block; width: 14px; height: 1px; background: currentColor; }
  .motto .snail { display: inline-block; width: 8px; height: 8px; border-radius: 50%; background: var(--gold); margin-left: 5px; }

  .contact { position: absolute; left: 28px; right: 20px; bottom: 17px; font-size: 6px; letter-spacing: .02em; white-space: nowrap; }
  .contact strong { font-weight: 400; color: #000; }
</style>
</head>
<body>

  <div class="piece card" style="left:103px; top:97px;">
    <div class="wordmark small" style="left:24px; top:80px;"><span class="name"><span class="line">The</span><span class="line">Corvella</span><span class="line">Spa</span></span><span class="descriptor">a boutique spa for Men &amp; Women</span></div>
  </div>
  <div class="piece sleeve" style="left:103px; top:97px;" role="img" aria-label="Sleeve with fine repeating arc pattern">
    <div class="motto" style="left:165px; top:104px;"><span class="lead"></span>Slow down, enjoy life.<span class="snail" role="img" aria-label="Golden snail"></span></div>
  </div>

  <div class="piece card" style="left:64px; top:328px;">
    <div class="wordmark small" style="left:24px; top:80px;"><span class="name"><span class="line">The</span><span class="line">Corvella</span><span class="line">Spa</span></span><span class="descriptor">a boutique spa for Men &amp; Women</span></div>
  </div>
  <div class="piece sleeve" style="left:103px; top:328px;" role="img" aria-label="Sleeve with fine repeating arc pattern">
    <div class="motto" style="left:165px; top:104px;"><span class="lead"></span>Slow down, enjoy life.<span class="snail" role="img" aria-label="Golden snail"></span></div>
  </div>

  <div class="piece card" style="left:452px; top:330px;">
    <div class="wordmark small" style="left:24px; top:80px;"><span class="name"><span class="line">The</span><span class="line">Corvella</span><span class="line">Spa</span></span><span class="descriptor">a boutique spa for Men &amp; Women</span></div>
    <div class="motto" style="left:160px; top:103px;"><span class="lead"></span>Slow down, enjoy life.<span class="snail" role="img" aria-label="Golden snail"></span></div>
  </div>

  <div class="piece card" style="left:799px; top:330px;">
    <div class="wordmark large" style="left:57px; top:72px;"><span class="name"><span class="line">The</span><span class="line">Corvella</span><span class="line">Spa</span></span><span class="descriptor">a boutique spa for Men &amp; Women</span></div>
    <p class="contact">3817 Birch Lane . linden vale, new york 10999 . (555) 462 3085 . <strong>info@thecorvella spa.com</strong></p>
  </div>

  <div class="piece sleeve plain" style="left:103px; top:561px;" role="img" aria-label="Sleeve reverse with fine repeating arc pattern">
    <div class="wordmark medium" style="left:80px; top:70px;"><span class="name"><span class="line">The</span><span class="line">Corvella</span><span class="line">Spa</span></span><span class="descriptor">a boutique spa for Men &amp; Women</span></div>
  </div>

</body>
</html>
```